Carton Box Packaging For Motorcycle Brake Shoe - Vorenta Brand

Packaging Dimensions: 125mm (H) x 125mm (W) x 31mm (D)
We would like to design a genuine Carton box Packaging for motorcycle Brake Shoe.
This is a critical part of the motorcycle, so we need the packaging to reflect elegant impression.
Vorenta, is one of the leading companies for manufacturing Motorcycles, located in Egypt. Our company is offering high-quality products, the best in the local market, with very competitive prices.
We have a limited time to get this project done, So we Highly appreciate receiving your designs ASAP.
Target Market(s)
Economical Motorcycle Buyers
Font styles to use
Colors
Designer to choose colors to be used in the design.
Look and feel
Each slider illustrates characteristics of the customer's brand and the style your logo design should communicate.

```html
<!DOCTYPE html>
<html lang="en">
<head>
<meta charset="utf-8">
<title>Vorenta Motorcycle Brake Shoe – Carton Dieline</title>
<link rel="stylesheet" href="https://fonts.googleapis.com/css2?family=Exo+2:ital,wght@0,800;1,800;1,900&family=Arimo:wght@400&display=swap">
<style>
  :root {
    --paper: #ffffff;
    --ink: #0d0d0d;
    --steel: #8f9092;
    --steel-dark: #4a4a4c;
    --cut-line: #9a9a9a;
    --label-edge: #7d7d7d;
    --shoe-light: #b9b4a6;
    --shoe-dark: #6e6a60;
  }
  * { box-sizing: border-box; margin: 0; padding: 0; }
  html, body { width: 935px; height: 1200px; overflow: hidden; background: var(--paper); }
  .dieline { position: relative; width: 935px; height: 1200px; }

  .panel {
    position: absolute;
    border: 1px solid var(--cut-line);
    background: linear-gradient(135deg, var(--steel) 0%, var(--steel-dark) 50%, var(--steel) 100%);
  }

  .label {
    position: absolute;
    background: var(--paper);
    border: 1px solid var(--label-edge);
    border-radius: 7px;
    overflow: hidden;
  }
  .label-content {
    position: absolute;
    left: 50%; top: 50%;
    display: flex; align-items: center; justify-content: space-between;
    padding: 0 10px;
  }
  .rot-90 { transform: translate(-50%, -50%) rotate(90deg); }
  .rot-270 { transform: translate(-50%, -50%) rotate(-90deg); }
  .rot-180 { transform: translate(-50%, -50%) rotate(180deg); }
  .rot-0 { transform: translate(-50%, -50%); }

  .product-title {
    font-family: "Exo 2", sans-serif;
    font-style: italic;
    font-weight: 900;
    color: var(--ink);
    text-transform: uppercase;
    line-height: 1.08;
    letter-spacing: 0.5px;
  }

  .brand-mark { display: flex; flex-direction: column; align-items: center; gap: 3px; }
  .brand-mark .dot {
    border-radius: 50%;
    background: var(--steel-dark);
  }
  .brand-name {
    font-family: "Exo 2", sans-serif;
    font-style: normal;
    font-weight: 800;
    color: var(--ink);
    text-transform: uppercase;
    letter-spacing: 1px;
  }

  .shoe-photo {
    border-radius: 50%;
    background: radial-gradient(circle, var(--paper) 38%, var(--shoe-light) 42%, var(--shoe-dark) 70%, var(--shoe-light) 100%);
  }

  .info-box {
    position: absolute;
    left: 367px; top: 722px; width: 314px; height: 314px;
    background: var(--paper);
    border: 1px solid var(--label-edge);
    border-radius: 10px;
    font-family: "Arimo", sans-serif;
    font-size: 12.5px;
    line-height: 17px;
    color: var(--ink);
    text-align: center;
    padding-top: 101px;
  }
  .info-box p + p { margin-top: 17px; }

  .hero-brand {
    position: absolute;
    left: 432px; top: 165px; width: 184px; height: 220px;
    display: flex; flex-direction: column; align-items: center; justify-content: center; gap: 16px;
  }
  .hero-brand .dot { width: 140px; height: 140px; border-radius: 50%; background: var(--paper); }
  .hero-brand .brand-name { font-size: 30px; color: var(--paper); letter-spacing: 3px; }
</style>
</head>
<body>
<main class="dieline">

  <!-- top row flaps -->
  <div class="panel" style="left:206px;top:36px;width:106px;height:94px" role="img" aria-label="Black and grey diagonal tile pattern"></div>
  <div class="panel" style="left:312px;top:30px;width:425px;height:100px" role="img" aria-label="Black and grey diagonal tile pattern"></div>
  <div class="panel" style="left:737px;top:36px;width:106px;height:94px" role="img" aria-label="Black and grey diagonal tile pattern"></div>

  <div class="label" style="left:324px;top:40px;width:399px;height:86px">
    <div class="label-content rot-180" style="width:399px;height:86px">
      <div class="brand-mark"><span class="dot" style="width:34px;height:34px"></span><span class="brand-name" style="font-size:9px">Vorenta</span></div>
      <div class="product-title" style="font-size:25px">Motorcycle<br>Brake Shoe</div>
      <div class="shoe-photo" role="img" aria-label="Photo of motorcycle brake shoe pair" style="width:70px;height:70px"></div>
    </div>
  </div>

  <!-- middle row: sides and front -->
  <div class="panel" style="left:206px;top:135px;width:106px;height:426px" role="img" aria-label="Black and grey diagonal tile pattern"></div>
  <div class="panel" style="left:312px;top:130px;width:425px;height:431px" role="img" aria-label="Black and grey diagonal tile pattern"></div>
  <div class="panel" style="left:737px;top:135px;width:106px;height:426px" role="img" aria-label="Black and grey diagonal tile pattern"></div>

  <div class="label" style="left:216px;top:148px;width:86px;height:399px">
    <div class="label-content rot-90" style="width:399px;height:86px">
      <div class="brand-mark"><span class="dot" style="width:36px;height:36px"></span><span class="brand-name" style="font-size:9px">Vorenta</span></div>
      <div class="product-title" style="font-size:27px">Motorcycle<br>Brake Shoe</div>
      <div class="shoe-photo" role="img" aria-label="Photo of motorcycle brake shoe pair" style="width:74px;height:74px"></div>
    </div>
  </div>

  <div class="hero-brand">
    <span class="dot"></span>
    <span class="brand-name">Vorenta</span>
  </div>

  <div class="label" style="left:324px;top:412px;width:399px;height:123px">
    <div class="label-content rot-0" style="width:399px;height:123px;padding:0 12px 0 14px">
      <div class="product-title" style="font-size:38px">Motorcycle<br>Brake Shoe</div>
      <div class="shoe-photo" role="img" aria-label="Photo of motorcycle brake shoe pair" style="width:110px;height:110px"></div>
    </div>
  </div>

  <div class="label" style="left:748px;top:148px;width:86px;height:399px">
    <div class="label-content rot-270" style="width:399px;height:86px">
      <div class="brand-mark"><span class="dot" style="width:36px;height:36px"></span><span class="brand-name" style="font-size:9px">Vorenta</span></div>
      <div class="product-title" style="font-size:27px">Motorcycle<br>Brake Shoe</div>
      <div class="shoe-photo" role="img" aria-label="Photo of motorcycle brake shoe pair" style="width:74px;height:74px"></div>
    </div>
  </div>

  <!-- lower flap row -->
  <div class="panel" style="left:206px;top:566px;width:106px;height:94px" role="img" aria-label="Black and grey diagonal tile pattern"></div>
  <div class="panel" style="left:312px;top:561px;width:425px;height:102px" role="img" aria-label="Black and grey diagonal tile pattern"></div>
  <div class="panel" style="left:737px;top:566px;width:106px;height:94px" role="img" aria-label="Black and grey diagonal tile pattern"></div>

  <div class="label" style="left:324px;top:570px;width:399px;height:87px">
    <div class="label-content rot-0" style="width:399px;height:87px">
      <div class="brand-mark"><span class="dot" style="width:40px;height:40px"></span><span class="brand-name" style="font-size:9px">Vorenta</span></div>
      <div class="product-title" style="font-size:26px">Motorcycle<br>Brake Shoe</div>
      <div class="shoe-photo" role="img" aria-label="Photo of motorcycle brake shoe pair" style="width:72px;height:72px"></div>
    </div>
  </div>

  <!-- back panel with side flaps -->
  <div class="panel" style="left:206px;top:663px;width:637px;height:429px" role="img" aria-label="Black and grey diagonal tile pattern"></div>
  <div class="info-box">
    <p>Part name<br>Part code</p>
    <p>Manufacturer name<br>Manufacturer address<br>Manufacturer phone</p>
  </div>

  <!-- bottom tuck flap -->
  <div class="panel" style="left:312px;top:1092px;width:425px;height:91px" role="img" aria-label="Black and grey diagonal tile pattern"></div>

</main>
</body>
</html>
```